VORLEN Website Design

We need a website designed for our company VORLEN. We are a luxury lifestyle club that will provide benefits and services for our members. The site should be clean & sleek, preferably using black and white (or darker colors). (example sites: brimvale.example, tusko.example)

Here is a link of a sample page I did using wix. (https://pelmundry4.sitebuild.example/mypage) This can be used to get a general idea.

Target Market(s)

Upper Middle Class in the United States

Number of Pages Required

5+ page

Font styles to use
Sans Serif
Other font styles liked:
• Arial (or other similar fonts)

Requirements
Must have
• A clean design that is eye-catching and speaks to our company.
Nice to have
• Ideas for copy.

```html
<!DOCTYPE html>
<html lang="en">
<head>
<meta charset="utf-8">
<title>VORLEN — A Members Only Lifestyle Club</title>
<link rel="stylesheet" href="https://fonts.googleapis.com/css2?family=Montserrat:wght@300;400;500;600;700&family=Open+Sans:wght@400;600&display=swap">
<style>
:root{
  --bg:#13111b;
  --bg-deep:#0f0d16;
  --card:#1a1824;
  --accent:#3b2f86;
  --white:#ffffff;
  --muted:#cfcdd8;
  --ghost:rgba(255,255,255,0.045);
  --line:rgba(255,255,255,0.75);
}
*{box-sizing:border-box;margin:0;padding:0}
html,body{width:1200px;height:3120px;overflow:hidden;background:var(--bg)}
body{position:relative;font-family:"Open Sans",Arial,sans-serif;color:var(--white)}
.abs{position:absolute}

/* Hero */
.hero{left:0;top:0;width:1200px;height:655px;overflow:hidden}
.hero-photo{position:absolute;inset:0;background:
  radial-gradient(ellipse 260px 160px at 150px 420px,rgba(200,20,50,.55),transparent 70%),
  radial-gradient(ellipse 200px 140px at 1020px 470px,rgba(210,30,60,.5),transparent 70%),
  radial-gradient(ellipse 160px 90px at 480px 360px,rgba(140,40,200,.45),transparent 70%),
  radial-gradient(ellipse 300px 140px at 900px 260px,rgba(70,90,150,.4),transparent 70%),
  linear-gradient(180deg,#120d15 0%,#241016 55%,#1a0a10 100%)}
.hero-shade{position:absolute;inset:0;background:linear-gradient(180deg,rgba(0,0,0,.45),rgba(0,0,0,.15) 40%,rgba(0,0,0,.2))}
.nav{left:0;top:0;width:1200px;height:150px}
.logo{left:112px;top:56px;font-family:Montserrat,Arial,sans-serif;font-weight:700;font-size:30px;letter-spacing:1px}
.menu{right:110px;top:64px;display:flex;gap:34px;align-items:center;font-family:Montserrat,Arial,sans-serif;font-weight:500;font-size:16px;letter-spacing:.5px}
.hero-kicker{left:0;width:1200px;top:188px;text-align:center;font-family:Montserrat,Arial,sans-serif;font-weight:500;font-size:48px;letter-spacing:1px}
.hero-title{left:0;width:1200px;top:252px;text-align:center;font-family:Montserrat,Arial,sans-serif;font-weight:700;font-size:94px;letter-spacing:1px;line-height:1}
.dots{left:566px;top:581px;display:flex;gap:4px}
.dot{width:14px;height:14px;border-radius:50%;border:2px solid var(--white)}
.dot.active{background:var(--white)}

/* About */
.about-box{left:112px;top:749px;width:974px;height:458px;border:2px solid rgba(255,255,255,.55)}
.ghost{font-family:Montserrat,Arial,sans-serif;font-weight:700;color:var(--ghost);text-align:center;white-space:nowrap;letter-spacing:2px}
.section-title{font-family:Montserrat,Arial,sans-serif;font-weight:400;text-align:center;white-space:nowrap;letter-spacing:1px}
.about-ghost{left:0;width:1200px;top:812px;font-size:90px}
.about-title{left:0;width:1200px;top:838px;font-size:58px}
.about-sub{left:0;width:1200px;top:928px;text-align:center;font-size:22px;font-weight:600}
.about-copy{left:230px;width:740px;top:988px;text-align:center;font-size:15px;line-height:29px;color:var(--muted)}
.btn{display:flex;align-items:center;justify-content:center;border:2px solid var(--white);border-radius:32px;background:var(--bg);font-family:Montserrat,Arial,sans-serif;font-weight:700;font-size:16px;letter-spacing:.5px}
.about-apply{left:517px;top:1177px;width:166px;height:60px}

/* Services */
.services-ghost{left:0;width:1200px;top:1340px;font-size:98px}
.services-title{left:0;width:1200px;top:1370px;font-size:58px}
.card{width:314px;height:266px;background:var(--card);display:flex;flex-direction:column;align-items:center;padding-top:44px}
.card svg{width:76px;height:76px;fill:var(--accent)}
.card-label{margin-top:26px;font-family:Montserrat,Arial,sans-serif;font-weight:500;font-size:26px;line-height:34px;text-align:center;letter-spacing:1px}
.view-more{left:510px;top:2104px;width:180px;height:60px}

/* Apply */
.apply-photo{left:599px;top:2273px;width:601px;height:550px;background:
  radial-gradient(ellipse 200px 160px at 450px 90px,rgba(40,190,210,.55),transparent 70%),
  radial-gradient(ellipse 260px 200px at 280px 300px,rgba(190,130,90,.45),transparent 70%),
  radial-gradient(ellipse 220px 120px at 280px 470px,rgba(120,60,30,.5),transparent 70%),
  linear-gradient(135deg,#2a1a14,#120c0c 60%,#1d1411)}
.apply-ghost{left:112px;top:2345px;font-size:80px;text-align:left}
.apply-title{left:112px;top:2372px;font-size:58px;text-align:left}
.field{background:var(--white);color:#777;font-size:13px;padding:10px 14px}
.submit{left:112px;top:2698px;width:127px;height:48px}

/* Footer */
.socials{left:475px;top:2897px;display:flex;gap:8px}
.social{width:50px;height:50px;border-radius:50%;border:2px solid var(--line)}
.contact{left:0;width:1200px;top:2980px;display:flex;justify-content:center;align-items:center;gap:12px;font-size:15px}
.contact svg{width:14px;height:14px;fill:var(--white);margin-right:6px;vertical-align:-2px}
.links{left:0;width:1200px;top:3017px;text-align:center;font-size:14px;word-spacing:2px}
.links span{margin:0 14px}
.copyright{left:0;width:1200px;top:3054px;text-align:center;font-size:14px}
</style>
</head>
<body>

<section class="abs hero">
  <div class="hero-photo" role="img" aria-label="Photo of a dimly lit luxury lounge with red chairs and glowing table lights"></div>
  <div class="hero-shade"></div>
</section>

<header class="abs nav">
  <div class="abs logo">VORLEN</div>
  <nav class="abs menu">
    <span>HOME</span><span>ABOUT</span><span>SERVICES &amp; BENEFITS</span><span>APPLY</span><span>CONTACT</span>
    <svg width="18" height="18" viewBox="0 0 20 20"><circle cx="8" cy="8" r="6" fill="none" stroke="#fff" stroke-width="2.5"/><line x1="12.5" y1="12.5" x2="18" y2="18" stroke="#fff" stroke-width="3"/></svg>
  </nav>
</header>

<h1 class="abs hero-kicker">A MEMBERS ONLY</h1>
<div class="abs hero-title">LIFESTYLE CLUB</div>
<div class="abs dots"><span class="dot active"></span><span class="dot"></span><span class="dot"></span><span class="dot"></span><span class="dot"></span></div>

<section>
  <div class="abs about-box"></div>
  <div class="abs ghost about-ghost">ABOUT VORLEN</div>
  <h2 class="abs section-title about-title">ABOUT VORLEN</h2>
  <p class="abs about-sub">The ultimate full service lifestyle club</p>
  <p class="abs about-copy">VORLEN was formed to bring the best services, experiences, and exclusive opportunities to our members. With everything from private member events to private jet travel, the perks of being a VORLEN member are unmatched. Professional athletes, artists, musicians, corporate professionals: Our members come from diverse backgrounds. Comprehensive services like 24/7 concierge, accountants, attorneys, private advisers, planners, investment advisors and more.</p>
  <div class="abs btn about-apply">APPLY</div>
</section>

<section>
  <div class="abs ghost services-ghost">SERVICES &amp; BENEFITS</div>
  <h2 class="abs section-title services-title">SERVICES AND BENEFITS</h2>

  <div class="abs card" style="left:112px;top:1491px">
    <svg viewBox="0 0 24 24"><path d="M5 1h14a2 2 0 0 1 2 2v18a2 2 0 0 1-2 2H5a2 2 0 0 1-2-2V3a2 2 0 0 1 2-2zm1 2v5h12V3zm0 7v3h3v-3zm4.5 0v3h3v-3zM15 10v3h3v-3zM6 14.5v3h3v-3zm4.5 0v3h3v-3zm4.5 0v3h3v-3zM6 19v2h3v-2zm4.5 0v2h3v-2zm4.5 0v2h3v-2z"/></svg>
    <div class="card-label">ACCOUNTING<br>SERVICES</div>
  </div>
  <div class="abs card" style="left:443px;top:1491px">
    <svg viewBox="0 0 24 24"><path d="M2 2h2v18h18v2H2zm4 10h3v7H6zm4.5-4h3v11h-3zM15 11h3v8h-3zm4.5-5H22v13h-2.5z"/></svg>
    <div class="card-label">INVESTMENT<br>SERVICES</div>
  </div>
  <div class="abs card" style="left:774px;top:1491px">
    <svg viewBox="0 0 24 24"><path d="M9.5 1.5l6 6-2.5 2.5-6-6zM5 6l3.5-3.5 6 6L11 12zm5.5 6.5l2.5-2.5 9.5 9.5-2.5 2.5zM2.5 8.5L5 6l6 6-2.5 2.5z"/></svg>
    <div class="card-label">LAWYER<br>SERVICES</div>
  </div>
  <div class="abs card" style="left:112px;top:1774px">
    <svg viewBox="0 0 24 24"><path d="M4 1h16v22h-6v-4h-4v4H4zm3 3v2h2V4zm4 0v2h2V4zm4 0v2h2V4zM7 8v2h2V8zm4 0v2h2V8zm4 0v2h2V8zm-8 4v2h2v-2zm4 0v2h2v-2zm4 0v2h2v-2z"/></svg>
    <div class="card-label">REAL ESTATE<br>SERVICES</div>
  </div>
  <div class="abs card" style="left:443px;top:1774px">
    <svg viewBox="0 0 24 24"><path d="M6 1h2v3h8V1h2v3h3a1 1 0 0 1 1 1v17a1 1 0 0 1-1 1H3a1 1 0 0 1-1-1V5a1 1 0 0 1 1-1h3zM4 9v12h16V9zm1.5 1.5h3v2.5h-3zm4.5 0h3v2.5h-3zm4.5 0h3v2.5h-3zM5.5 14.5h3v2.5h-3zm4.5 0h3v2.5h-3zm4.5 0h3v2.5h-3zM5.5 18.5h3V20h-3zm4.5 0h3V20h-3zm4.5 0h3V20h-3z"/></svg>
    <div class="card-label">24/7<br>CONCIERGE</div>
  </div>
  <div class="abs card" style="left:774px;top:1774px">
    <svg viewBox="0 0 24 24"><path d="M21 3c1 1-.5 3.5-2 5l-2 2 2.5 9-2 2-4.5-7-3 3 .5 3.5-1.5 1.5-2-4-4-2L4.5 14.5 8 15l3-3-7-4.5 2-2 9 2.5 2-2c1.5-1.5 4-3 5-2z"/></svg>
    <div class="card-label">PRIVATE<br>JET TRAVEL</div>
  </div>

  <div class="abs btn view-more">VIEW MORE</div>
</section>

<section>
  <div class="abs apply-photo" role="img" aria-label="Photo of club members laughing together at a candlelit bar table"></div>
  <div class="abs ghost apply-ghost">APPLY</div>
  <h2 class="abs section-title apply-title">APPLY</h2>
  <div class="abs field" style="left:112px;top:2479px;width:217px;height:42px">First Name</div>
  <div class="abs field" style="left:339px;top:2479px;width:218px;height:42px">Last Name</div>
  <div class="abs field" style="left:112px;top:2533px;width:217px;height:42px">Email Address</div>
  <div class="abs field" style="left:339px;top:2533px;width:218px;height:42px">Phone Number</div>
  <div class="abs field" style="left:112px;top:2587px;width:445px;height:82px">Message</div>
  <div class="abs btn submit">SUBMIT</div>
</section>

<footer>
  <div class="abs socials"><span class="social"></span><span class="social"></span><span class="social"></span><span class="social"></span><span class="social"></span></div>
  <div class="abs contact">
    <span><svg viewBox="0 0 24 24"><path d="M12 1a8 8 0 0 1 8 8c0 6-8 14-8 14S4 15 4 9a8 8 0 0 1 8-8zm0 5a3 3 0 1 0 0 6 3 3 0 0 0 0-6z"/></svg>42 Larkspur Lane Dunmore, NSW 2911.</span><span>|</span>
    <span><svg viewBox="0 0 24 24"><path d="M6.6 10.8a15 15 0 0 0 6.6 6.6l2.2-2.2a1 1 0 0 1 1-.25 11.4 11.4 0 0 0 3.6.6 1 1 0 0 1 1 1V20a1 1 0 0 1-1 1A17 17 0 0 1 3 4a1 1 0 0 1 1-1h3.5a1 1 0 0 1 1 1 11.4 11.4 0 0 0 .6 3.6 1 1 0 0 1-.25 1z"/></svg>1 800 555 0142</span><span>|</span>
    <span><svg viewBox="0 0 24 24"><path d="M2 4h20v16H2zm2 2v.5l8 5.5 8-5.5V6zm0 3v9h16V9l-8 5.5z"/></svg>info@vorlen.example</span>
  </div>
  <div class="abs links">Help<span>|</span>FAQ<span>|</span>Support<span>|</span>Sitemap<span>|</span>Terms Of Use<span>|</span>Privacy Statement</div>
  <div class="abs copyright">VORLEN© 2018 All rights reserved.</div>
</footer>

</body>
</html>
```